Premium Gold Vodka Label Design

English ------------------- We need a label for a Vodka Bottle. Its a sparkling premium vodka with gold inside. The design should look premium. We tried it on our selves but it looks horrible. Therefore we need your help. The current name is corvelle K, but we are open for any better suggestion. We attached the selfmade design. The label will be printed on the bottle. We have other design jobs for you (logo, other sorts)! English ------------------------ We need a label for a vodka bottle. This is a premium vodka which is offset with gold. The design should look like this. We have tried so far and failed. That is why we need your support. The name is so far corvelle K. If you have better suggestions we would be pleased about other suggestions / ideas. In the appendix the failed design is stored. The label is to be applied by screen printing. In the case of good work follow-up projects are guaranteed (logo, other varieties, etc)!
Updates

Reason: We need more time for the decision.

Target Market(s)

USA

Colors

Designer to choose colors to be used in the design.

Requirements
Must have
• English ------------------------ The needed text is on our selfmade label that is attached. English ------------------------ The required texts are stored in the attached design.
Nice to have
• English ------------------------ Transparent places are allowed because we want to print the label on the bottom. English ------------------------ As the label is applied by screen printing, transparent areas are also possible.

```html
<!DOCTYPE html>
<html lang="en">
<head>
<meta charset="utf-8">
<title>corvelle K – 24kt Premium Gold Sparkling Vodka Label</title>
<link rel="stylesheet" href="https://fonts.googleapis.com/css2?family=Cinzel:wght@400;600;700&family=Cormorant+Garamond:wght@500;600&display=swap">
<style>
  :root {
    --backdrop: #f4f1ea;
    --gold-deep: #9c6a1c;
    --gold-mid: #c99a3a;
    --gold-light: #ecca74;
    --gold-glow: #f7e2a0;
    --accent-yellow: #f6c719;
    --cream: #fff6dc;
    --ink-shadow: rgba(80, 50, 10, 0.35);
  }
  html, body {
    margin: 0;
    padding: 0;
    width: 701px;
    height: 1200px;
    overflow: hidden;
    background: var(--backdrop);
  }
  .canvas {
    position: relative;
    width: 701px;
    height: 1200px;
  }
  .label {
    position: absolute;
    left: 190px;
    top: 20px;
    width: 320px;
    height: 1160px;
    background:
      linear-gradient(90deg, var(--gold-deep) 0%, var(--gold-mid) 18%, var(--gold-light) 45%, var(--gold-glow) 55%, var(--gold-mid) 82%, var(--gold-deep) 100%);
    box-shadow: 0 6px 22px rgba(0,0,0,0.18);
    text-align: center;
    font-family: "Cinzel", serif;
  }
  .ornament-area {
    position: absolute;
    left: 40px;
    top: 30px;
    width: 240px;
    height: 330px;
    border-radius: 120px 120px 40px 40px;
    background: radial-gradient(circle at 50% 35%, var(--gold-glow) 0%, var(--gold-light) 40%, var(--gold-mid) 100%);
    opacity: 0.75;
  }
  .brand-name {
    position: absolute;
    left: 0;
    right: 0;
    top: 400px;
    margin: 0;
    font-family: "Cinzel", serif;
    font-weight: 700;
    font-size: 40px;
    letter-spacing: 1px;
    color: var(--accent-yellow);
  }
  .karat {
    position: absolute;
    left: 0;
    right: 0;
    top: 458px;
    margin: 0;
    font-weight: 700;
    font-size: 28px;
    color: var(--accent-yellow);
    font-family: "Cormorant Garamond", serif;
  }
  .descriptor {
    position: absolute;
    left: 0;
    right: 0;
    top: 505px;
    margin: 0;
    font-family: "Cinzel", serif;
    font-weight: 400;
    font-size: 27px;
    line-height: 34px;
    color: var(--cream);
    text-shadow: 0 1px 2px var(--ink-shadow);
  }
  .product {
    position: absolute;
    left: 0;
    right: 0;
    top: 585px;
    margin: 0;
    font-family: "Cinzel", serif;
    font-weight: 400;
    font-size: 46px;
    letter-spacing: 2px;
    color: var(--cream);
    text-shadow: 0 1px 2px var(--ink-shadow);
  }
  .process {
    position: absolute;
    left: 0;
    right: 0;
    top: 665px;
    margin: 0;
    font-family: "Cinzel", serif;
    font-weight: 600;
    font-size: 19px;
    color: var(--accent-yellow);
  }
  .process .amp {
    font-size: 30px;
    vertical-align: -4px;
  }
  .origin {
    position: absolute;
    left: 0;
    right: 0;
    top: 760px;
    margin: 0;
    font-family: "Cormorant Garamond", serif;
    font-weight: 600;
    font-size: 17px;
    color: var(--cream);
  }
  .specs {
    position: absolute;
    left: 24px;
    right: 24px;
    top: 786px;
    display: flex;
    justify-content: space-between;
    font-family: "Cormorant Garamond", serif;
    font-weight: 600;
    font-size: 15px;
    color: var(--cream);
  }
  .specs .volume {
    font-size: 19px;
  }
</style>
</head>
<body>
  <main class="canvas">
    <section class="label">
      <div class="ornament-area" role="img" aria-label="Gold mandala ornament crowning the label"></div>
      <h1 class="brand-name">corvelle K</h1>
      <p class="karat">24kt</p>
      <p class="descriptor">Premium Gold<br>Sparkling</p>
      <p class="product">VODKA</p>
      <p class="process">DISTILLED <span class="amp">8</span> FILTERED</p>
      <p class="origin">Made in Germany</p>
      <div class="specs">
        <span>40% Alc./Vol.</span>
        <span class="volume">200ml</span>
        <span>80 Proof</span>
      </div>
    </section>
  </main>
</body>
</html>
```